Quiet ridge balance Business cards - yoga studio

We need business cards for our yoga studio Quietridge Balance.
We would like to see designs that include the colour blue and our logo.
The business card should communicate a feeling of strength and calm

Industry/Entity Type

Business

Requirements
Must have
• The business card must include
"Helena Moorcroft - Director"
and
"27 Tamarind Crescent
Fernvale
VIC 3794
Ph - 0451 806 214"

```html
<!DOCTYPE html>
<html lang="en">
<head>
<meta charset="utf-8">
<title>Quietridge Balance – Business Card Design 2A</title>
<link href="https://fonts.googleapis.com/css2?family=Questrial&display=swap" rel="stylesheet">
<style>
  :root {
    --brand-teal: #6ce3d1;
    --card-border: #e6e6e6;
    --paper: #ffffff;
    --screen-tint: #e8f2f0;
  }
  * { margin: 0; padding: 0; box-sizing: border-box; }
  html, body {
    width: 929px;
    height: 1200px;
    overflow: hidden;
    background: var(--paper);
    font-family: "Questrial", "Century Gothic", sans-serif;
    color: var(--brand-teal);
  }
  .sheet { position: relative; width: 929px; height: 1200px; }

  .design-label {
    position: absolute;
    left: 66px;
    top: 28px;
    font-size: 46px;
    font-weight: 400;
    letter-spacing: 0.5px;
    line-height: 1;
  }

  .card {
    position: absolute;
    left: 58px;
    width: 815px;
    height: 509px;
    border: 3px solid var(--card-border);
    background: var(--paper);
    overflow: hidden;
  }
  .card--front { top: 92px; }
  .card--back { top: 643px; }

  /* Front */
  .brand-dot {
    position: absolute;
    left: 50%;
    top: 56px;
    width: 190px;
    height: 190px;
    margin-left: -95px;
    border-radius: 50%;
    background: var(--brand-teal);
  }
  .brand-name {
    position: absolute;
    left: 0;
    right: 0;
    top: 306px;
    text-align: center;
    font-size: 64px;
    line-height: 1;
    font-weight: 400;
    white-space: nowrap;
  }
  .brand-tagline {
    position: absolute;
    left: 0;
    right: 0;
    top: 440px;
    text-align: center;
    font-size: 19px;
    letter-spacing: 1px;
  }

  /* Back */
  .contact-person {
    position: absolute;
    left: 60px;
    top: 124px;
    width: 342px;
    text-align: right;
  }
  .contact-person__name {
    font-size: 44px;
    line-height: 1.1;
    white-space: nowrap;
  }
  .contact-person__role {
    font-size: 30px;
    letter-spacing: 1.5px;
    margin-top: 4px;
  }

  .contact-row {
    position: absolute;
    left: 50px;
    display: flex;
    align-items: flex-start;
  }
  .contact-row__icon {
    width: 30px;
    height: 34px;
    flex: 0 0 30px;
    margin-right: 21px;
  }
  .contact-row__text {
    font-size: 31px;
    line-height: 41px;
    letter-spacing: 2px;
    font-style: normal;
    white-space: nowrap;
  }
  .contact-row--address { top: 274px; }
  .contact-row--address .contact-row__icon { margin-top: 3px; }
  .contact-row--phone { top: 408px; }
  .contact-row--phone .contact-row__icon { margin-top: 4px; }
  .small-caps { font-variant: small-caps; }

  .card-accent {
    position: absolute;
    left: 470px;
    top: 250px;
    width: 400px;
    height: 400px;
    border-radius: 50%;
    background: var(--brand-teal);
  }
</style>
</head>
<body>
<main class="sheet">
  <h1 class="design-label">DESIGN 2A</h1>

  <section class="card card--front" aria-label="Card front">
    <div class="brand-dot" aria-hidden="true"></div>
    <p class="brand-name">Quietridge Balance</p>
    <p class="brand-tagline">YOGA · FITNESS · AQUA</p>
  </section>

  <section class="card card--back" aria-label="Card back">
    <div class="contact-person">
      <p class="contact-person__name">Helena Moorcroft</p>
      <p class="contact-person__role">DIRECTOR</p>
    </div>

    <div class="contact-row contact-row--address">
      <svg class="contact-row__icon" viewBox="0 0 30 34" aria-hidden="true">
        <path d="M15 1C8 1 3 6 3 12.5 3 21 15 33 15 33S27 21 27 12.5C27 6 22 1 15 1Z" fill="var(--brand-teal)"/>
        <circle cx="15" cy="12" r="4" fill="var(--paper)"/>
      </svg>
      <address class="contact-row__text small-caps">
        27 Tamarind Crescent<br>
        Fernvale<br>
        VIC 3794
      </address>
    </div>

    <div class="contact-row contact-row--phone">
      <svg class="contact-row__icon" viewBox="0 0 30 34" aria-hidden="true">
        <rect x="6" y="1" width="18" height="32" rx="3" fill="var(--brand-teal)"/>
        <rect x="9" y="5" width="12" height="21" fill="var(--screen-tint)"/>
        <circle cx="15" cy="29.5" r="1.5" fill="var(--paper)"/>
      </svg>
      <p class="contact-row__text">0451 806 214</p>
    </div>

    <div class="card-accent" aria-hidden="true"></div>
  </section>
</main>
</body>
</html>
```